Glow Up by Lakeside 21 day Challenge

We are having a Glow Up by Lakeside Challenge at our fitness studio. We need a poster design using the template attached as a reference. I have also included our Bromalux logo to put on the poster. Please DO NOT use the graphics in the flyer as we are expecting something much better :-)

-Size needed 11x17 with bleeding for printing

-We need this made in Photoshop (CS3 friendly) or at least delivered in PS as we might change some text or re-arrange the design later on.

-We need this in layers.

```html
<!DOCTYPE html>
<html lang="en">
<head>
<meta charset="utf-8">
<title>Glow Up by Lakeside 21 Day Challenge</title>
<link rel="stylesheet" href="https://fonts.googleapis.com/css2?family=Kanit:ital,wght@1,900&family=Ubuntu:wght@500;700&family=Noticia+Text:ital,wght@1,400;1,700&family=Raleway:ital,wght@1,500&display=swap">
<style>
  :root {
    --dark-brown: #2a1a12;
    --band-blue: #1f8fd6;
    --band-teal: #2fc0c4;
    --band-green: #22c45a;
    --rust: #8a3415;
    --headline: #f7f5ef;
    --bullet-gold: #f2d24a;
    --body-light: #fbf6ea;
    --price-cream: #f1ead8;
    --quote-box: rgba(120, 40, 15, 0.55);
    --quote-border: rgba(240, 200, 160, 0.35);
  }
  html, body { margin: 0; padding: 0; overflow: hidden; background: #1a100b; }
  .poster {
    position: relative;
    width: 780px; height: 1200px; overflow: hidden;
    background:
      radial-gradient(ellipse at 30% 55%, #d99a2e 0%, rgba(217,154,46,0) 35%),
      radial-gradient(ellipse at 80% 80%, #c4501c 0%, rgba(196,80,28,0) 45%),
      linear-gradient(180deg, var(--dark-brown) 0%, #4a2312 30%, var(--rust) 60%, #7a2a12 85%, #5a1e0e 100%);
  }
  .bands { position: absolute; left: 0; top: 0; }
  .brand {
    position: absolute; left: 40px; top: 34px; z-index: 3;
    display: flex; align-items: center; gap: 10px;
    font-family: "Ubuntu", sans-serif; font-weight: 700;
    font-size: 30px; letter-spacing: 3px; color: var(--headline);
  }
  .brand-mark { width: 16px; height: 16px; background: var(--headline); }
  .headline {
    position: absolute; margin: 0; z-index: 3; white-space: nowrap;
    font-family: "Kanit", sans-serif; font-style: italic; font-weight: 900;
    color: var(--headline); line-height: 1;
    text-shadow: 4px 5px 0 rgba(0,0,0,0.35);
    transform-origin: left bottom;
  }
  .headline-1 { left: 150px; top: 100px; font-size: 132px; transform: rotate(-6deg); }
  .headline-2 { left: 64px; top: 275px; font-size: 124px; transform: rotate(-3deg); }
  .headline-3 { left: 56px; top: 455px; font-size: 80px; transform: rotate(5deg); }
  .athlete-photo { position: absolute; left: 478px; top: 200px; width: 292px; height: 425px; z-index: 1; }
  .runner-photo { position: absolute; left: 20px; top: 760px; width: 200px; height: 440px; opacity: 0.28; z-index: 1; }
  .offer { position: absolute; left: 0; width: 780px; text-align: center; margin: 0; z-index: 2; }
  .offer-title {
    top: 664px; font-family: "Ubuntu", sans-serif; font-weight: 700;
    font-size: 30.5px; line-height: 42px; color: var(--body-light);
    text-shadow: 2px 2px 0 rgba(0,0,0,0.75);
  }
  .benefits {
    top: 760px; list-style: none; padding: 0;
    font-family: "Noticia Text", serif; font-style: italic; font-weight: 700;
    font-size: 17px; color: var(--bullet-gold); text-transform: uppercase;
    text-shadow: 1px 1px 1px rgba(0,0,0,0.6);
  }
  .benefits li { line-height: 21px; margin-bottom: 20px; white-space: nowrap; }
  .price {
    top: 958px; font-family: "Ubuntu", sans-serif; font-weight: 500;
    font-size: 32px; color: var(--price-cream);
    text-shadow: 2px 2px 1px rgba(0,0,0,0.55);
  }
  .testimonial {
    position: absolute; left: 56px; top: 1018px; width: 672px; height: 64px; z-index: 2;
    box-sizing: border-box; margin: 0;
    background: var(--quote-box); border: 1px solid var(--quote-border);
    font-family: "Raleway", sans-serif; font-style: italic; font-weight: 500;
    font-size: 22px; line-height: 27px; color: var(--body-light);
    text-align: center; padding-top: 4px;
  }
  .cta {
    top: 1102px; font-family: "Ubuntu", sans-serif; font-weight: 700;
    font-size: 26px; line-height: 37px; color: var(--body-light);
    text-shadow: 2px 2px 1px rgba(0,0,0,0.6);
  }
  .cta-contact { font-family: "Noticia Text", serif; font-weight: 400; font-size: 22px; }
</style>
</head>
<body>
<main class="poster">
  <svg class="bands" width="780" height="700" viewBox="0 0 780 700" aria-hidden="true">
    <polygon points="0,90 780,26 780,202 0,282" fill="var(--band-blue)"/>
    <polygon points="0,268 780,192 780,398 0,452" fill="var(--band-teal)"/>
    <polygon points="0,432 780,382 780,664 0,560" fill="var(--band-green)"/>
  </svg>

  <div class="brand"><span class="brand-mark"></span>BROMALUX</div>

  <svg class="athlete-photo" viewBox="0 0 292 425" role="img" aria-label="Photo of a female athlete in a sprint start crouch, orange top and black leggings">
    <defs>
      <linearGradient id="athleteTone" x1="0" y1="0" x2="0" y2="1">
        <stop offset="0" stop-color="#d96a2a" stop-opacity="0.85"/>
        <stop offset="0.5" stop-color="#2a2226" stop-opacity="0.85"/>
        <stop offset="1" stop-color="#1d1a1f" stop-opacity="0.7"/>
      </linearGradient>
    </defs>
    <rect width="292" height="425" fill="url(#athleteTone)"/>
  </svg>

  <svg class="runner-photo" viewBox="0 0 200 440" role="img" aria-label="Faded photo of a smiling woman running in a green tank top">
    <defs>
      <linearGradient id="runnerTone" x1="0" y1="0" x2="0" y2="1">
        <stop offset="0" stop-color="#e7b98a"/>
        <stop offset="0.5" stop-color="#8a9a78"/>
        <stop offset="1" stop-color="#b06a40"/>
      </linearGradient>
    </defs>
    <rect width="200" height="440" fill="url(#runnerTone)"/>
  </svg>

  <h1 class="headline headline-1">GLOW UP</h1>
  <div class="headline headline-2">BY</div>
  <div class="headline headline-3">LAKESIDE</div>

  <h2 class="offer offer-title">DISCOVER THE SECRET TO A BEACH-READY BODY<br>IN JUST 21 DAYS!</h2>

  <ul class="offer benefits">
    <li>9 total training sessions designed to incinerate fat<br>off your midsection, thighs and arms</li>
    <li>21 days of nutritional guidance, including delicious recipes</li>
    <li>A success session to map out your individual plan for success</li>
    <li>Your very own personal accountability coach to ensure you get results</li>
  </ul>

  <p class="offer price">YOU GET ALL THIS -399$ VALUE- FOR ONLY 99$</p>

  <blockquote class="testimonial">I'VE NEVER BEEN MORE FIT IN MY LIFE—AT AGE 41!<br>~MARLA QUENBY</blockquote>

  <p class="offer cta">HURRY! SPACE IS LIMITED TO ONLY 20 PARTICIPANTS!!!<br>CLAIM YOUR SPOT NOW: <span class="cta-contact">www.stridehall.com - call 555-01</span></p>
</main>
</body>
</html>
```